Distinctinctive and nordic inspired container design for a new started health and active brand.

Our company name is ROVI and stands for "Reach Onward, Venture Inward". Our goal is to provide a no BS approach to Supplementation and specific problem solving products.

As a Danish based brand our key words is: "Minimalism", "clear lines", "Nordic colours i.eg. and as seen in canvas", "Purity", "simplicity", "design", "Functionality", "health", "clarity" and "calm".

This design is aimed at a two container product (AM) for "night" and (PM) for "day".
Design is focused on a rectangular shape with a rectangular shape lid that screws on to a uniform and harmonious design.
Colour wise we are most into matte "earth colors that can also be seen in canvas.
These can be singular or a mix in the design but we kindly ask to stay away from "bright and shiny" colours.
Logos and scriptures will be added as a 2D effect, with exception for the lid logo which we would to see retracted into the lid itself.

In a rendering design we would like two containers next to each other seen from different angles where one lid is screwed off and one is screwed on.
In addition we would like a single container rendering showing only PM and only AM.

Happy designing

Jesper & Bodil - ROVI

European and North american markets.
Target: Male and Female age group 18-50.

Health Product

Serif
Sans Serif

• Clear and distinctive profile
Matte colours
uniform and harmonious shape (rectangular base)
inspired by earth minerals colours and contours.
• 3D visual effect in rendering to better get a feel of the product
• Shiny colours or material indicators.

```html
<!DOCTYPE html>
<html lang="en">
<head>
<meta charset="utf-8">
<title>ROVI Container Labels</title>
<link rel="stylesheet" href="https://fonts.googleapis.com/css2?family=Arimo:wght@400;700&display=swap">
<style>
  :root {
    --page: #ffffff;
    --body: #c9c6c0;
    --body-edge: #b9b5ae;
    --cap: #d7d6d1;
    --cap-edge: #c3c1bb;
    --neck: #e6e8ea;
    --ink: #141414;
    --accent: #1f4e79;
    --art-dark: #1a1a1a;
    --art-mid: #8e8b86;
    --cap-white: #f4f4f2;
  }
  * { box-sizing: border-box; margin: 0; padding: 0; }
  html, body { width: 1200px; height: 833px; overflow: hidden; background: var(--page); }
  body { position: relative; font-family: "Arimo", Arial, sans-serif; color: var(--ink); }

  .bottle { position: absolute; top: 42px; height: 745px; }
  .bottle .cap {
    position: absolute; top: 0; height: 96px; background: var(--cap);
    border: 1px solid var(--cap-edge); border-radius: 8px 8px 3px 3px;
    display: flex; align-items: center; justify-content: center;
    font-weight: 700; font-size: 25px;
  }
  .bottle .cap--open { background: var(--neck); border-color: #d3d6d9; opacity: .9; }
  .bottle .neck {
    position: absolute; top: 96px; height: 33px; background: var(--neck);
    border: 1px solid #d3d6d9; border-radius: 4px;
  }
  .bottle .label {
    position: absolute; top: 129px; left: 0; right: 0; bottom: 0;
    background: var(--body); border: 1px solid var(--body-edge); border-radius: 8px;
  }

  .brand { position: absolute; left: 0; right: 0; top: 76px; text-align: center; }
  .brand__mark { display: inline-block; width: 12px; height: 12px; background: var(--accent); margin-bottom: 6px; }
  .brand__name { display: block; font-weight: 700; font-size: 30px; letter-spacing: 4px; line-height: 34px; }

  .facts {
    position: absolute; left: 37px; top: 196px; width: 186px;
    border-top: 1px solid #555; font-size: 6px; line-height: 7.3px;
  }
  .facts__title { font-weight: 700; font-size: 10px; line-height: 12px; }
  .facts__head, .facts__row { display: grid; grid-template-columns: 1fr 44px 36px; }
  .facts__head { border-top: 3px solid #333; border-bottom: 1px solid #333; font-weight: 700; text-align: right; }
  .facts__row span:not(:first-child) { text-align: right; }
  .facts__row--last { border-top: 2px solid #333; }
  .facts__note { border-top: 1px solid #333; border-bottom: 1px solid #555; }

  .art {
    position: absolute; border-radius: 50%;
    background: radial-gradient(circle closest-side at 50% 50%, var(--art-dark) 0 45%, var(--art-mid) 47% 98%, transparent 100%);
  }

  .vertical-mark { position: absolute; left: 115px; top: 246px; width: 18px; height: 18px; background: var(--accent); }
  .vertical-name {
    position: absolute; left: 97px; top: 300px; writing-mode: vertical-rl; transform: rotate(180deg);
    font-weight: 700; font-size: 56px; letter-spacing: 6px; line-height: 1;
  }

  .purpose { position: absolute; left: 0; right: 0; top: 160px; text-align: center; font-weight: 700; font-size: 15px; }
  .copy { position: absolute; left: 46px; top: 200px; width: 165px; font-size: 7.8px; line-height: 10px; font-weight: 700; }
  .copy__stat { float: left; font-size: 29px; line-height: 28px; font-weight: 400; margin-right: 5px; }

  .cap-top {
    position: absolute; left: 907px; top: 392px; width: 120px; height: 120px; border-radius: 50%;
    background: var(--cap-white); border: 1px solid #ddd; text-align: center;
  }
  .cap-top .art { left: 33px; top: 14px; width: 54px; height: 54px; }
  .cap-top__text { position: absolute; left: 0; right: 0; top: 74px; font-weight: 700; font-size: 21px; }
  .cap-side {
    position: absolute; left: 1043px; top: 432px; width: 124px; height: 80px;
    background: repeating-linear-gradient(90deg, var(--cap-white) 0 5px, #e6e6e4 5px 6px);
    border-radius: 6px; display: flex; align-items: center; justify-content: center;
    font-weight: 700; font-size: 21px;
  }
</style>
</head>
<body>

<section class="bottle bottle--facts" style="left:32px;width:254px;">
  <div class="cap" style="left:61px;width:138px;"></div>
  <div class="neck" style="left:51px;width:158px;"></div>
  <div class="label">
    <div class="brand"><span class="brand__mark"></span><span class="brand__name">ROVI</span></div>
    <div class="facts">
      <div class="facts__title">Supplement Facts</div>
      <div>Serving Size One tablet</div>
      <div class="facts__head"><span></span><span>Amount Per Serving</span><span>% Daily Value</span></div>
      <div class="facts__row"><span>Vitamin A (14% as beta-carotene)</span><span>3500 IU</span><span>70%</span></div>
      <div class="facts__row"><span>Vitamin C</span><span>60 mg</span><span>100%</span></div>
      <div class="facts__row"><span>Vitamin D (as Vitamin D3)</span><span>700 IU</span><span>175%</span></div>
      <div class="facts__row"><span>Vitamin E</span><span>22.5 IU</span><span>75%</span></div>
      <div class="facts__row"><span>Vitamin K</span><span>20 mcg</span><span>25%</span></div>
      <div class="facts__row"><span>Thiamin (B1)</span><span>1.35 mg</span><span>90%</span></div>
      <div class="facts__row"><span>Riboflavin (B2)</span><span>1.7 mg</span><span>100%</span></div>
      <div class="facts__row"><span>Niacin</span><span>18 mg</span><span>90%</span></div>
      <div class="facts__row"><span>Vitamin B6</span><span>3 mg</span><span>150%</span></div>
      <div class="facts__row"><span>Folic Acid</span><span>400 mcg</span><span>100%</span></div>
      <div class="facts__row"><span>Vitamin B12</span><span>18 mcg</span><span>300%</span></div>
      <div class="facts__row"><span>Biotin</span><span>75 mcg</span><span>25%</span></div>
      <div class="facts__row"><span>Pantothenic Acid</span><span>16 mg</span><span>160%</span></div>
      <div class="facts__row"><span>Calcium (elemental)</span><span>210 mg</span><span>21%</span></div>
      <div class="facts__row"><span>Iron</span><span>0 mg</span><span>0%</span></div>
      <div class="facts__row"><span>Magnesium</span><span>140 mg</span><span>35%</span></div>
      <div class="facts__row"><span>Zinc</span><span>15 mg</span><span>100%</span></div>
      <div class="facts__row"><span>Selenium</span><span>110 mcg</span><span>157%</span></div>
      <div class="facts__row"><span>Copper</span><span>2 mg</span><span>100%</span></div>
      <div class="facts__row"><span>Manganese</span><span>2 mg</span><span>100%</span></div>
      <div class="facts__row"><span>Chromium</span><span>120 mcg</span><span>100%</span></div>
      <div class="facts__row facts__row--last"><span>Lycopene</span><span>300 mcg</span><span>*</span></div>
      <div class="facts__note">*Daily Value not established</div>
    </div>
  </div>
</section>

<section class="bottle bottle--front" style="left:325px;width:252px;">
  <div class="cap" style="left:59px;width:136px;">MALE</div>
  <div class="neck" style="left:48px;width:156px;"></div>
  <div class="label">
    <div class="art" role="img" aria-label="Sun rising over stylised clouds illustration" style="left:78px;top:78px;width:96px;height:96px;"></div>
    <span class="vertical-mark"></span>
    <span class="vertical-name">ROVI</span>
  </div>
</section>

<section class="bottle bottle--purpose" style="left:615px;width:254px;">
  <div class="cap cap--open" style="left:66px;width:126px;"></div>
  <div class="neck" style="left:52px;width:154px;"></div>
  <div class="label">
    <div class="brand"><span class="brand__mark"></span><span class="brand__name">ROVI</span></div>
    <div class="purpose">PURPOSE</div>
    <p class="copy"><span class="copy__stat">99%</span>Lorem ipsum dolor sit amet, consec tetur adipiscing elit. Morbi ultricies molestie orci. Aenean purus mauris, sodales nec diam dignissim, porttitor laoreet enim. Aliquam id sollicitudin turpis. Vivamus aliquet elit sem, et ornare ex aliquam in. In cursus, felis non pretium molestie, tellus lacus facilisis metus, ut accumsan nisi nulla accumsan risus. Etiam id pharetra ante. Nunc sit amet ante id justo consequat tempor. Nullam pretium arcu eu hendrerit aliquam. Sed in purus eros.</p>
  </div>
</section>

<div class="cap-top">
  <div class="art" role="img" aria-label="Sun and cloud illustration recessed into the lid"></div>
  <span class="cap-top__text">AM</span>
</div>
<div class="cap-side">MALE</div>

</body>
</html>
```